Professional Reserve Fund Planners require print ad

The Accredited Lifecycle Budget Advising (ALB) designation is the only designated professional that has specific education in the preparation of reserve fund studies.
Reserve Fund Studies are mandatory for Condominiums across Canada and we want to promote our designation as a step above others performing studies and should be sought out by clients if they would like to have the best studies.
The advertising will require space for the Housing Stewardship Guild of Canada (HSGC) logo and the contact information for planners who have the accreditation.
Some points to consider: The designation has been in place since 1999. Specific training in the preparation of long term reserve fund studies with a specific focus on financial fundamentals, technical proficiency, investing reserves appropriately and legislation.
This will be a full page magazine ad for a trade publication called Strata Ledger by PrintHollow. Thanks.
Please note that the ads i have uploaded are simply ads that I feel capture the essence of what I am trying to achieve. I believe the ads I have uploaded are indicating a feeling of trust in the designation THEY are promoting. I want our designation ad to feel the same. You are out looking for someone to perform a reserve fund study. You can find the same old schmuck or you can find someone who has invested time and money seeking a better education and the designation ALB shows dedication, ethical standards and educational level that should give clients the feeling they are getting the best of the best.
For property managers and a Board of Directors, a properly prepared and timely reserve fund study will keep the Board of Directors and/or owners off their back. I always use the concept of "hiring us makes your job easier" and words or phrases like value-add partner, service provider, collaboration, reasonable, achievable.
Condominium owners looking for professional reserve fund study services.
Condominium Board of Directors
Condominium Property Managers

```html
<!DOCTYPE html>
<html lang="en">
<head>
<meta charset="utf-8">
<title>Accredited Lifecycle Budget Advisors – Print Ad</title>
<link rel="stylesheet" href="https://fonts.googleapis.com/css2?family=Philosopher:wght@400;700&family=Open+Sans:ital,wght@0,700;1,300&display=swap">
<style>
  :root {
    --ink-navy: #262160;
    --headline-light: #e6e6e8;
    --tagline-white: #f2f2f2;
    --sky-yellow: #e6d670;
    --sky-green: #9fd0b0;
    --sky-peach: #e4b48e;
    --sky-mauve: #a98aa6;
    --sky-blue: #b4ccd1;
    --city-grey: #8a8e94;
    --city-dark: #6d6f76;
    --logo-ink: #111111;
  }
  html, body {
    margin: 0;
    padding: 0;
    overflow: hidden;
    background: #ffffff;
  }
  .ad {
    position: relative;
    width: 900px;
    height: 1200px;
    overflow: hidden;
    font-family: "Philosopher", sans-serif;
  }
  .ad__backdrop {
    position: absolute;
    inset: 0;
    background: linear-gradient(180deg,
      var(--sky-yellow) 0%,
      var(--sky-green) 12%,
      var(--sky-peach) 22%,
      var(--sky-blue) 30%,
      var(--sky-mauve) 36%,
      var(--sky-blue) 42%,
      var(--city-grey) 58%,
      var(--city-grey) 75%,
      var(--city-dark) 100%);
  }
  .slogan {
    position: absolute;
    right: 82px;
    top: 128px;
    text-align: right;
    color: var(--ink-navy);
    margin: 0;
  }
  .slogan__main {
    display: block;
    font-weight: 700;
    font-size: 106px;
    line-height: 1;
    letter-spacing: 1px;
  }
  .slogan__sub {
    display: block;
    font-weight: 400;
    font-size: 60px;
    line-height: 1;
    margin-top: 2px;
  }
  .slogan__since {
    display: block;
    font-family: "Open Sans", sans-serif;
    font-weight: 700;
    font-size: 18px;
    margin-top: 4px;
    margin-right: 6px;
  }
  .focus-areas {
    position: absolute;
    right: 44px;
    top: 732px;
    margin: 0;
    padding: 0;
    list-style: none;
    text-align: right;
    font-family: "Open Sans", sans-serif;
    font-style: italic;
    font-weight: 300;
    font-size: 21px;
    line-height: 29.5px;
    color: var(--tagline-white);
  }
  .directory-heading {
    position: absolute;
    left: 127px;
    top: 860px;
    margin: 0;
    font-weight: 700;
    font-size: 55px;
    line-height: 68px;
    color: var(--headline-light);
  }
  .org-sign {
    position: absolute;
    left: 26px;
    top: 1117px;
    display: flex;
    align-items: center;
    gap: 12px;
  }
  .org-sign__mark {
    width: 66px;
    height: 66px;
    background: var(--logo-ink);
  }
  .org-sign__name {
    font-family: "Open Sans", sans-serif;
    font-weight: 700;
    font-size: 17px;
    line-height: 21px;
    color: var(--logo-ink);
  }
</style>
</head>
<body>
  <main class="ad">
    <div class="ad__backdrop" role="img" aria-label="Abstract flowing bands of colour over a soft grey city skyline of condominium towers"></div>

    <h1 class="slogan">
      <span class="slogan__main">peace of mind</span>
      <span class="slogan__sub">proven quality</span>
      <span class="slogan__since">since 1999</span>
    </h1>

    <ul class="focus-areas">
      <li>financial fundamentals</li>
      <li>technical proficiency</li>
      <li>legislation</li>
    </ul>

    <h2 class="directory-heading">Accredited Lifecycle Budget<br>Advisors in your area:</h2>

    <div class="org-sign">
      <div class="org-sign__mark"></div>
      <div class="org-sign__name">Housing Stewardship Guild of Canada<br>Guilde canadienne de l’intendance</div>
    </div>
  </main>
</body>
</html>
```